Managed Service Provider need new business cards

We are a small Maanged Service Provider of IT Services and need a new fresh design for our business cards. We want something impossible, fun and professional :)
Our services has a large range, but we are always fun and make sure our customers both get their issue sorted and also feel like they are "catching up with an old friend".
All our cards in the past has always been all black, with red and we need something fresher.
The back of card, we would like just a small list of what we do i think, but if someone has a better idea, please do something cool with the back of the card:
Managed IT Services
Productivity Solutions
Data Backup and Recovery
IT System Maintenance
Managed IT Security
More details can be found on our website tqnetworks.com.au
Industry/Entity Type
It Company
Contact Information for Business Card
Name: Dwayne Falstrup
Title: Director
Phone: 03 6193 4827
Mobile: 0412 587 239
Email: dwayne@tqnetworks.com.au
Web: www.tqnetworks.com.au

```html
<!DOCTYPE html>
<html lang="en">
<head>
<meta charset="utf-8">
<title>TQ Networks — Business Card</title>
<link rel="stylesheet" href="https://fonts.googleapis.com/css2?family=Josefin+Sans:wght@400;600;700&display=swap">
<style>
  :root {
    --brand-red: #d6202b;
    --accent-red: #e33a46;
    --card-black: #1b1b1c;
    --card-white: #efefef;
    --text-light: #e8e8e8;
    --stage: #2a2a2b;
  }
  * { margin: 0; padding: 0; box-sizing: border-box; }
  html, body { width: 1200px; height: 900px; overflow: hidden; }
  body {
    background: var(--stage);
    font-family: "Josefin Sans", sans-serif;
    display: flex;
    flex-direction: column;
    align-items: center;
    justify-content: center;
    gap: 40px;
  }
  .card {
    position: relative;
    width: 700px;
    height: 400px;
    border-radius: 28px;
    overflow: hidden;
    background: var(--card-black);
    box-shadow: 0 18px 40px rgba(0,0,0,.45);
  }
  .card-front__panel { position: absolute; inset: 0; }
  .brand {
    position: absolute;
    display: flex;
    align-items: center;
    gap: 14px;
    color: var(--brand-red);
    font-weight: 700;
    letter-spacing: .5px;
  }
  .brand__dot {
    border-radius: 50%;
    background: var(--brand-red);
  }
  .card-front .brand { left: 48px; top: 46px; font-size: 48px; }
  .card-front .brand__dot { width: 22px; height: 22px; }
  .contact {
    position: absolute;
    right: 44px;
    top: 250px;
    text-align: right;
  }
  .contact__name {
    color: var(--accent-red);
    font-weight: 600;
    font-size: 26px;
    line-height: 1;
  }
  .contact__title {
    color: var(--text-light);
    font-size: 16px;
    margin: 4px 0 10px;
  }
  .contact__list { list-style: none; }
  .contact__item {
    display: flex;
    justify-content: flex-end;
    align-items: center;
    gap: 10px;
    color: var(--text-light);
    font-size: 15px;
    line-height: 22px;
  }
  .contact__icon {
    width: 18px; height: 18px;
    border-radius: 50%;
    background: var(--accent-red);
    display: inline-flex;
    align-items: center;
    justify-content: center;
  }
  .contact__icon svg { width: 11px; height: 11px; }
  .card-back .brand {
    left: 0; right: 0;
    top: 110px;
    justify-content: center;
    font-size: 64px;
  }
  .card-back .brand__dot { width: 28px; height: 28px; }
  .services {
    position: absolute;
    left: 0; right: 0;
    top: 230px;
    text-align: center;
    color: var(--text-light);
    font-size: 17px;
    line-height: 30px;
  }
  .services__item::before {
    content: "";
    display: inline-block;
    width: 7px; height: 7px;
    border-radius: 50%;
    background: var(--brand-red);
    margin: 0 9px 3px 12px;
    vertical-align: middle;
  }
</style>
</head>
<body>

<section class="card card-front" aria-label="Business card front">
  <svg class="card-front__panel" viewBox="0 0 700 400" aria-hidden="true">
    <path fill="var(--card-white)" d="M0 0 H575 C520 20 500 60 540 95 C590 140 640 170 640 215 C640 250 590 250 520 235 C440 215 360 190 310 200 C270 210 290 280 260 330 C240 370 200 395 170 400 H0 Z"/>
    <path fill="none" stroke="var(--accent-red)" stroke-width="7" stroke-linecap="round" d="M575 0 C520 20 500 60 540 95 C590 140 640 170 640 215 C640 250 590 250 520 235 C440 215 360 190 310 200 C270 210 290 280 260 330 C240 370 200 395 170 400"/>
  </svg>

  <div class="brand">
    <span class="brand__dot"></span>
    <span class="brand__name">TQ Networks</span>
  </div>

  <div class="contact">
    <p class="contact__name">Dwayne Falstrup</p>
    <p class="contact__title">Director</p>
    <ul class="contact__list">
      <li class="contact__item">03 6193 4827
        <span class="contact__icon"><svg viewBox="0 0 12 12"><path fill="#1b1b1c" d="M1 4 C1 2 3 1 6 1 C9 1 11 2 11 4 L9 5 L8 3.5 H4 L3 5 Z M3 6 H9 L10 11 H2 Z"/></svg></span>
      </li>
      <li class="contact__item">0412 587 239
        <span class="contact__icon"><svg viewBox="0 0 12 12"><rect x="3" y="1" width="6" height="10" rx="1.2" fill="none" stroke="#1b1b1c" stroke-width="1.4"/></svg></span>
      </li>
      <li class="contact__item">dwayne@tqnetworks.com.au
        <span class="contact__icon"><svg viewBox="0 0 12 12"><rect x="1" y="2.5" width="10" height="7" fill="none" stroke="#1b1b1c" stroke-width="1.3"/><path d="M1 2.5 L6 7 L11 2.5" fill="none" stroke="#1b1b1c" stroke-width="1.3"/></svg></span>
      </li>
      <li class="contact__item">www.tqnetworks.com.au
        <span class="contact__icon"><svg viewBox="0 0 12 12"><circle cx="6" cy="6" r="4.6" fill="none" stroke="#1b1b1c" stroke-width="1.3"/><path d="M1.4 6 H10.6 M6 1.4 C3.5 4 3.5 8 6 10.6 C8.5 8 8.5 4 6 1.4" fill="none" stroke="#1b1b1c" stroke-width="1"/></svg></span>
      </li>
    </ul>
  </div>
</section>

<section class="card card-back" aria-label="Business card back">
  <div class="brand">
    <span class="brand__dot"></span>
    <span class="brand__name">TQ Networks</span>
  </div>
  <div class="services">
    <p><span class="services__item">Managed IT Services</span><span class="services__item">Productivity Solutions</span><span class="services__item">Data Backup and Recovery</span></p>
    <p><span class="services__item">IT System Maintenance</span><span class="services__item">Managed IT Security</span></p>
  </div>
</section>

</body>
</html>
```